Dermatology Office Business Card Update

Updating some information on the current business card. Do not adjust font type. Need both rounded rectangle and rounded square card files. In addition, must have separate file for both rectangle and square cards for gold foil printing.1. Update phone number with: 555-318-27602. Remove email address3. Add this website to be listed under quillbrookdermatology.example:jilluxe.com4. Under updated phone number, add the flickvue logo in color and then a space and the following text: @dermjill5. Gold foil should be inclusive of the outline of the butterfly wings on the front. Also should put a small hyphen that is also gold foil under the cursive Nora Belcastro, MD and before the block lettering begins.Back of card remains the samePlease feel free to contact me with any questions!

Target Market(s)

Patients

Contact Information for Business Card

Just needs some updates along with files for gold foil printing

Requirements
Must have
• Updating some information on the current business card. Do not adjust font type. Need both rounded rectangle and rounded square card files. In addition, must have separate file for both rectangle and square cards for gold foil printing.
• 1. Update phone number with: 555-318-2760
• 2. Remove email address
• 3. Add this website to be listed under quillbrookdermatology.example:
• norvatek.example
• 4. Under updated phone number, add the flickvue logo in color and then a space and the following text: @docnorabel
• 5. Gold foil should be inclusive of the outline of the butterfly wings on the front. Also should put a small hyphen that is also gold foil under the cursive Nora Belcastro, MD and before the block lettering begins.
• Back of card remains the same
• Please feel free to contact me with any questions!

```html
<!DOCTYPE html>
<html lang="en">
<head>
<meta charset="utf-8">
<title>Quillbrook Dermatology – Business Card</title>
<link href="https://fonts.googleapis.com/css2?family=Lexend:wght@300;400&display=swap" rel="stylesheet">
<style>
  :root {
    --backdrop: #231b1f;
    --card-white: #f6f5f2;
    --navy: #24355a;
    --rose: #c4949a;
    --mauve-light: #b58a90;
    --mauve-dark: #7a4a58;
    --plum: #6e6384;
    --gold: #c9a44a;
    --gold-light: #e6cf86;
  }
  * { margin: 0; padding: 0; box-sizing: border-box; }
  html, body { width: 1200px; height: 800px; overflow: hidden; }
  body {
    background: var(--backdrop);
    font-family: "Lexend", sans-serif;
    position: relative;
  }
  .card {
    position: absolute;
    top: 194px;
    width: 411px;
    height: 410px;
    border-radius: 32px;
    overflow: hidden;
  }
  /* Front */
  .card-front { left: 166px; }
  .front-wash {
    position: absolute; inset: 0;
    background:
      radial-gradient(circle at 30% 25%, var(--mauve-light) 0%, transparent 60%),
      linear-gradient(150deg, #a87680 0%, var(--mauve-dark) 55%, var(--plum) 100%);
  }
  .front-mark {
    position: absolute; left: 0; right: 0; top: 160px;
    text-align: center;
    color: #ffffff;
    font-weight: 300;
    font-size: 26px;
    letter-spacing: 5px;
    line-height: 1.35;
  }
  .front-tagline {
    position: absolute; left: 0; right: 0; top: 290px;
    text-align: center;
    color: #ffffff;
    font-weight: 400;
    font-size: 17px;
    letter-spacing: 4px;
  }
  /* Back */
  .card-back { left: 622px; background: var(--card-white); color: var(--navy); text-align: center; }
  .brand-lockup {
    position: absolute; left: 0; right: 0; top: 124px;
    font-weight: 400;
    font-size: 19px;
    letter-spacing: 3.5px;
    line-height: 24px;
    color: var(--navy);
  }
  .gold-rule {
    position: absolute; left: 50%; height: 1.5px;
    background: linear-gradient(90deg, transparent, var(--gold) 20%, var(--gold-light) 50%, var(--gold) 80%, transparent);
    transform: translateX(-50%);
  }
  .rule-brand { top: 195px; width: 190px; }
  .doctor-name {
    position: absolute; left: 0; right: 0; top: 226px;
    font-size: 21px; letter-spacing: 3px; font-weight: 400;
    white-space: nowrap;
  }
  .doctor-name .credential { color: var(--rose); }
  .rule-name { top: 260px; width: 170px; }
  .contact-line {
    position: absolute; left: 0; right: 0; top: 270px;
    display: flex; justify-content: center; align-items: center; gap: 14px;
    font-size: 21px; letter-spacing: 1px;
    white-space: nowrap;
  }
  .contact-line .dot { color: var(--rose); }
  .social {
    display: flex; align-items: center; gap: 6px;
    font-size: 15px; letter-spacing: 0.3px;
  }
  .social-network { color: var(--rose); }
  .social-circle { width: 9px; height: 9px; border-radius: 50%; background: var(--rose); }
  .websites {
    position: absolute; left: 0; right: 0; top: 322px;
    color: var(--rose);
    font-size: 18px; letter-spacing: 0.5px; line-height: 22px; font-weight: 300;
    white-space: nowrap;
  }
  .back-band {
    position: absolute; left: 0; right: 0; bottom: 0; height: 25px;
    background: linear-gradient(90deg, var(--navy) 0%, #6c6386 35%, var(--mauve-light) 75%, var(--rose) 100%);
  }
</style>
</head>
<body>
  <section class="card card-front">
    <div class="front-wash" role="img" aria-label="Soft rose and plum watercolour wash"></div>
    <div class="front-mark">QUILLBROOK<br>DERMATOLOGY</div>
    <div class="front-tagline">RENEWING WITHIN</div>
  </section>

  <section class="card card-back">
    <div class="brand-lockup">QUILLBROOK<br>DERMATOLOGY</div>
    <div class="gold-rule rule-brand"></div>

    <div class="doctor-name">NORA BELCASTRO, <span class="credential">MD</span></div>
    <div class="gold-rule rule-name"></div>

    <div class="contact-line">
      <span class="phone">555<span class="dot">.</span>318<span class="dot">.</span>2760</span>
      <span class="social">
        <span class="social-circle"></span>
        <span class="social-network">flickvue</span>
        <span class="handle">@docnorabel</span>
      </span>
    </div>

    <div class="websites">
      quillbrookdermatology.example<br>norvatek.example
    </div>

    <div class="back-band" role="img" aria-label="Navy to rose watercolour strip"></div>
  </section>
</body>
</html>
```